Innovative WordPress for a non-profit organization dedicated to providing healthcare to the less for

Bright Harbor Aid is a small non-profit organization. BHA's core mission is to provide free medical and dental care to the less fortunate. Aside from providing healthcare, BHA also helps build infrastructure such as orphanage, cancer centers, water wells and small homes for the homeless. As a non-profit, BHA has been sponsoring various social programs to help those in need. From building infrastructure to health care and most recently micro-finance, the BHA team is helping to GIve Back to the community at person at a time.

BHA is growing and needs help to restructure for the future. The corporate website design is the first step in a new branding strategy for the company.

BHA current website is divided into three specific target areas:
1. Mission: This area is dedicated to provide information about medical and dental mission hosted by BHA.

2. Infrastructure. This area is dedicated to provide information about infrastructure programs supported and completed by the BHA team. The projects includes orphanage, cancer centers. water wells, micro-finance, small homes for the homeless...etc.

3. Special Projects. This area is used to showcase specific short term projects which might come up.

Aside from the specific three target area, BHA also needs a NEWS area where news about BHA can be published.

Please put your thinking cape on and help produce the next generation WordPress template for Bright Harbor Aid. Your design will great enhance the level of volunteers recruited and also increase the level of help that BHA can provide for other.

For a quick glance at the BHA website today, please visit http://www.bhaexample.org. The BHA team is looking for a fresh design.

Thank you very much for taking the time to help BHA advance its mission of helping those in need.

Reason: Seeking more variety in design. Design needs to have a donate button, sponsors area, news, welcome message, 3 primary functions (mission, infrastructure, and specials projects). The BHA logo is available. Please note, you have the option to NOT use the colors associated with BHA logo. Thank you for helping with designing the new site.

Non-Profit

Requirements
Must have
• 1. Donate Now button.
2. Primary focus areas: MISSION / INFRASTRUCTURE / SPECIAL PROJECTS
3. News & Events
4. Welcome Message area
5. Sponsors area - place to add sponsor logos

Nice to have
• 1. Photo of the Month: Used to show a specific photo to represent events or functions completed by the BHA team.

Please show sample of one level down. For example, what does the page look like when I click the MISSION link.

```html
<!DOCTYPE html>
<html lang="en">
<head>
<meta charset="utf-8">
<title>Bright Harbor Aid</title>
<link rel="stylesheet" href="https://fonts.googleapis.com/css2?family=Open+Sans:wdth,wght@75,300&family=Arimo:wght@400;700&display=swap">
<style>
:root{
  --green:#0a8f3c;
  --yellow:#f2d31b;
  --red:#e8202a;
  --grey-card:#858585;
  --ink:#222;
  --text:#444;
  --muted:#777;
  --band:#ececec;
  --black:#000;
  --white:#fff;
}
*{margin:0;padding:0;box-sizing:border-box}
html,body{width:943px;height:1200px;overflow:hidden}
body{position:relative;background:var(--white);font-family:Arimo,Arial,sans-serif;color:var(--text)}
.abs{position:absolute}
.cond{font-family:"Open Sans",Arimo,sans-serif;font-weight:300;font-stretch:75%}

/* header */
.site-header{left:0;top:0;width:943px;height:120px;background:linear-gradient(#fff 70%,#f0f0f0)}
.brand{left:94px;top:36px;display:flex;align-items:center;gap:10px}
.brand-dot{width:30px;height:30px;border-radius:50%;background:var(--green)}
.brand-name{font-size:24px;font-weight:700;color:var(--ink);letter-spacing:.2px}
.brand-tag{left:99px;top:79px;font-size:8.5px;color:var(--muted);letter-spacing:.4px}
.donate{left:697px;top:39px;width:140px;height:32px;background:var(--green);color:#fff;border-radius:2px;font-size:17px;display:flex;align-items:center;justify-content:center}
.main-nav{top:89px;font-size:12px;color:var(--ink)}
.main-nav.active::after{content:"";position:absolute;left:0;right:0;top:17px;height:3px;background:var(--green)}
.stripe{left:0;width:943px;height:5px;display:flex}
.stripe span:nth-child(1){width:344px;background:var(--green)}
.stripe span:nth-child(2){width:246px;background:var(--yellow)}
.stripe span:nth-child(3){flex:1;background:var(--red)}

/* hero */
.hero{left:0;top:125px;width:943px;height:299px;background:var(--black)}
.hero-photo{left:404px;top:125px;width:539px;height:299px;background:radial-gradient(ellipse at 45% 45%,#8a8a8a 0%,#3c3c3c 45%,#000 80%)}
.hero-title{left:136px;top:168px;font-size:68px;color:#fff;line-height:1}
.hero-lead{left:136px;top:238px;font-size:32px;color:#fff;line-height:39px}
.hero-sub{left:134px;top:319px;font-size:15.5px;color:#fff;line-height:22px}

/* focus areas */
.focus-band{left:0;top:424px;width:943px;height:120px;background:linear-gradient(#f4f4f4,#e4e4e4)}
.card{top:438px;width:262px;height:94px;color:#fff;box-shadow:0 6px 6px -4px rgba(0,0,0,.35)}
.card.mission{left:68px;background:var(--green)}
.card.infra{left:341px;background:var(--grey-card)}
.card.special{left:613px;background:var(--red)}
.card-icon{position:absolute;left:17px;top:22px;width:50px;height:50px;border-radius:50%;background:#fff;display:flex;align-items:center;justify-content:center}
.card h3{position:absolute;left:77px;top:5px;font-size:21px;line-height:26px}
.card p{position:absolute;left:77px;top:33px;width:175px;font-size:9.5px;line-height:12px;height:36px;overflow:hidden}
.card a{position:absolute;left:77px;top:70px;font-size:8px;color:#fff;text-decoration:underline}

/* welcome */
.welcome{left:0;top:544px;width:943px;height:149px;background:var(--band);border-top:1px solid #ddd;border-bottom:1px solid #ddd}
.welcome p{position:absolute;left:95px;top:11px;width:753px;text-align:center;font-size:22px;line-height:26px;color:#444}
.join{left:397px;top:646px;width:149px;height:35px;border:1px solid #bbb;border-radius:3px;background:linear-gradient(#fff,#dcdcdc);box-shadow:0 4px 5px -2px rgba(0,0,0,.3);font-size:21px;color:#333;display:flex;align-items:center;justify-content:center}

/* content columns */
.col-title{top:713px;display:flex;align-items:center;gap:10px;font-size:19px;font-weight:400;color:var(--ink)}
.about-text{left:95px;top:753px;width:191px;height:198px;overflow:hidden;font-size:9.6px;line-height:16.3px;text-align:justify;hyphens:auto;-webkit-hyphens:auto;color:var(--text)}
.about-text b{font-weight:400;color:var(--green)}
.more{height:17px;padding:0 5px;border:1px solid #bbb;border-radius:2px;background:linear-gradient(#fff,#e6e6e6);font-size:8.5px;color:#333;display:flex;align-items:center}
.item{width:260px}
.thumb{position:absolute;left:0;top:0;width:81px;height:60px}
.date{font-size:12px;color:#888}
.item h4{font-size:12px;font-weight:400;color:var(--ink);margin-top:3px}
.item p{font-size:9.5px;line-height:12px;color:#555;margin-top:2px}
.news .body{position:absolute;left:94px;top:0;width:160px}

/* footer */
.footer{left:0;top:1010px;width:943px;height:128px;background:linear-gradient(#e9e9e9,#fafafa 40%,#fff)}
.f-col h5{font-size:16px;font-weight:400;color:var(--ink);margin-bottom:8px}
.f-col li{list-style:none;font-size:9.5px;line-height:12px;color:#777}
.channel{display:flex;align-items:center;gap:8px;font-size:9.5px;color:#777;height:20px}
.channel i{width:11px;height:11px;background:#aaa;display:block}
.bottom{left:0;top:1143px;width:943px;height:57px;background:var(--black);color:#fff;font-size:8.5px;text-align:center;padding-top:20px}
</style>
</head>
<body>

<header class="abs site-header"></header>
<div class="abs brand"><span class="brand-dot"></span><span class="brand-name">Bright Harbor Aid</span></div>
<div class="abs brand-tag">SERVING THE DISADVANTAGE COMMUNITY</div>
<div class="abs donate">DONATE NOW</div>
<nav>
  <span class="abs main-nav active" style="left:340px">HOME</span>
  <span class="abs main-nav" style="left:391px">ABOUT US</span>
  <span class="abs main-nav" style="left:470px">MISSION</span>
  <span class="abs main-nav" style="left:539px">SPECIAL PROJECTS</span>
  <span class="abs main-nav" style="left:669px">INFRASTRUCTURE</span>
  <span class="abs main-nav" style="left:792px">EVENTS</span>
</nav>
<div class="abs stripe" style="top:120px"><span></span><span></span><span></span></div>

<section>
  <div class="abs hero"></div>
  <div class="abs hero-photo" role="img" aria-label="Black and white portrait photograph of a child in need"></div>
  <h1 class="abs hero-title cond">BHA</h1>
  <p class="abs hero-lead cond">Lorem ipsum dolor sit amet,<br>consectetur adipiscing elit.</p>
  <p class="abs hero-sub cond">Pellentesque habitant morbi tristique senectus et netus et<br>malesuada fames ac turpis egestas.</p>
</section>

<section>
  <div class="abs focus-band"></div>
  <div class="abs card mission">
    <div class="card-icon"><svg width="26" height="26" viewBox="0 0 26 26"><path d="M24 2 2 11l8 3 2 9 4-6 6 4z" fill="#0a8f3c"/></svg></div>
    <h3 class="cond">Mission</h3>
    <p>Through the years, Bright Harbor Aid has hosted numerous different types of dental/medical missions. Most recently</p>
    <a>Learn more</a>
  </div>
  <div class="abs card infra">
    <div class="card-icon"><svg width="28" height="26" viewBox="0 0 28 26"><path d="M14 1 2 7v2h24V7z M4 11h3v9H4z M10 11h3v9h-3z M15 11h3v9h-3z M21 11h3v9h-3z M2 22h24v3H2z" fill="#858585"/></svg></div>
    <h3 class="cond">Infrastructure</h3>
    <p>Lakeview Cancer Center – Marlow HouseAside from hosting various dental and medical missions through out the</p>
    <a>Learn more</a>
  </div>
  <div class="abs card special">
    <div class="card-icon"><svg width="26" height="26" viewBox="0 0 26 26"><rect x="2" y="2" width="22" height="22" rx="5" fill="#e8202a"/><path d="M11 7h4v4h4v4h-4v4h-4v-4H7v-4h4z" fill="#fff"/></svg></div>
    <h3 class="cond">Special Projects</h3>
    <p>Lakeview Cancer Center – Marlow HouseAside from hosting various dental and medical missions through out the</p>
    <a>Learn more</a>
  </div>
</section>

<section class="abs welcome">
  <p class="cond">BHA's core mission is to provide free medical and dental care to the less fortunate. Aside from providing healthcare, BHA also helps build infrastructure such as orphanage, cancer centers, water wells and small homes for the homeless.</p>
</section>
<div class="abs join cond">Join us Now</div>

<section>
  <h2 class="abs col-title" style="left:95px"><svg width="30" height="18"><circle cx="15" cy="9" r="8" fill="#bbb"/></svg>About us</h2>
  <p class="abs about-text" lang="en"><b>Bright Harbor Aid (BHA)</b> is a non-profit 501(c)(3) organization dedicated to providing health-care, human services, and educational assistance to underprivileged communities. We work in collaboration with various groups and non-governmental organizations (NGOs) to deliver humanitarian goods, services, and relief to impoverished regions. The team is comprised of professionals with a broad spectrum of experiences. The combined mission trips of our team ..</p>
  <div class="abs more" style="left:95px;top:960px">More info</div>

  <h2 class="abs col-title" style="left:347px"><svg width="20" height="22"><path d="M2 1h11l5 5v15H2z" fill="#bbb"/><path d="M5 9h10M5 13h10M5 17h7" stroke="#fff" stroke-width="1.5"/></svg>Latest News</h2>
  <div class="abs item news" style="left:348px;top:759px">
    <div class="thumb" role="img" aria-label="Photo of a volunteer doctor with a patient" style="background:linear-gradient(135deg,#b89a7a,#4a3b30)"></div>
    <div class="body"><div class="date">10 JUN, 2014</div><h4>Lorem ipsum dolor sit amet</h4><p>Fusce diam mauris, pulvinar a nulla vitae, ornare sagittis leo.</p></div>
  </div>
  <div class="abs item news" style="left:348px;top:834px">
    <div class="thumb" role="img" aria-label="Group photo of volunteers in green shirts" style="background:linear-gradient(135deg,#8fc04a,#3f6a2a)"></div>
    <div class="body"><div class="date">06 MAY, 2014</div><h4>Lorem ipsum dolor sit amet</h4><p>Fusce diam mauris, pulvinar a nulla vitae, ornare sagittis leo.</p></div>
  </div>
  <div class="abs item news" style="left:348px;top:909px">
    <div class="thumb" role="img" aria-label="Photo of a dental clinic event with children" style="background:linear-gradient(135deg,#6d8fb8,#3a3150)"></div>
    <div class="body"><div class="date">14 APR, 2014</div><h4>Lorem ipsum dolor sit amet</h4><p>Fusce diam mauris, pulvinar a nulla vitae, ornare sagittis leo.</p></div>
  </div>
  <div class="abs more" style="left:347px;top:980px">More info</div>

  <h2 class="abs col-title" style="left:646px"><svg width="20" height="20"><rect x="1" y="3" width="18" height="16" fill="#bbb"/><path d="M1 7h18M5 1v4M15 1v4" stroke="#fff" stroke-width="1.5"/><path d="M5 1v3M15 1v3" stroke="#bbb" stroke-width="2"/></svg>Upcoming Events</h2>
  <div class="abs item" style="left:649px;top:756px"><div class="date">10 JUN, 2014</div><h4>Lorem ipsum dolor sit amet</h4><p>Fusce diam mauris, pulvinar a nulla vitae,<br>ornare sagittis leo.</p></div>
  <div class="abs item" style="left:649px;top:826px"><div class="date">10 JUN, 2014</div><h4>Lorem ipsum dolor sit amet</h4><p>Fusce diam mauris, pulvinar a nulla vitae,<br>ornare sagittis leo.</p></div>
  <div class="abs item" style="left:649px;top:901px"><div class="date">10 JUN, 2014</div><h4>Lorem ipsum dolor sit amet</h4><p>Fusce diam mauris, pulvinar a nulla vitae,<br>ornare sagittis leo.</p></div>
  <div class="abs more" style="left:651px;top:968px">More info</div>
</section>

<footer>
  <div class="abs footer"></div>
  <div class="abs f-col" style="left:94px;top:1021px"><h5>Quick links</h5><ul><li>Home</li><li>About Us</li><li>Mission</li><li>Special Projects</li><li>Infrastructure</li><li>Events</li></ul></div>
  <div class="abs f-col" style="left:252px;top:1021px"><h5>Information</h5><ul><li>Volantaring</li><li>How is Behind BHA</li><li>Out Team</li><li>Services</li><li>How to join us</li></ul></div>
  <div class="abs f-col" style="left:421px;top:1021px"><h5>Contact info</h5><ul><li>BHA</li><li>123 dummy bulding</li><li>4th floor, Dummy Street</li><li>Dummy Street United State</li></ul></div>
  <div class="abs f-col" style="left:646px;top:1021px"><h5>Other Channels</h5>
    <div class="channel"><i style="border-radius:50%"></i>Follow us on Chirper</div>
    <div class="channel"><i></i>FaceSpace</div>
    <div class="channel"><i></i>ViewTube</div>
  </div>
  <div class="abs stripe" style="top:1138px"><span></span><span></span><span></span></div>
  <div class="abs bottom">© 2014 Bright Harbor Aid</div>
</footer>

</body>
</html>
```